Varno Building Pty Ltd need an Identity!

We need a logo design for a building company based in Sydney, Australia. In addition - Business Card Layout. The colour scheme is to be black and red and communicate a professional yet 'hands on' approach to building.

Target Market(s)

Architects, Home Owners, Developers

Industry/Entity Type

Construction

Font styles to use
Serif
Sans Serif

Colors
ec1f27

Requirements
Must have
• Clear logo and professional direction.
Nice to have
• Use of initials as a possible logo
Should not have
• Graphics/pictures of houses, house roofs etc. Can be an abstracted form of a building.

```html
<!DOCTYPE html>
<html lang="en">
<head>
<meta charset="utf-8">
<title>Varno Building Pty Ltd – Business Cards</title>
<link href="https://fonts.googleapis.com/css2?family=Saira+Semi+Condensed:wght@400;500;700&family=Inter:wght@400&display=swap" rel="stylesheet">
<style>
  :root {
    --brand-red: #d9251d;
    --paper: #fafafa;
    --backdrop: #cbcbcb;
    --ink: #2e2e2e;
    --ink-soft: #555555;
  }
  html, body {
    margin: 0;
    width: 1200px;
    height: 1005px;
    overflow: hidden;
    background: var(--backdrop);
  }
  .card {
    position: absolute;
    left: 220px;
    width: 760px;
    height: 434px;
    box-shadow: 0 6px 18px rgba(0,0,0,0.18);
  }
  .card--front { top: 48px; background: var(--brand-red); }
  .card--back  { top: 522px; background: var(--paper); }

  .wordmark {
    position: absolute;
    text-align: center;
    font-family: "Saira Semi Condensed", sans-serif;
    font-weight: 500;
    line-height: 1;
  }
  .wordmark__square {
    width: 70px;
    height: 70px;
    margin: 0 auto 18px;
  }
  .wordmark__name {
    font-size: 64px;
    letter-spacing: 6px;
  }
  .wordmark__sub {
    font-size: 24px;
    letter-spacing: 1px;
    margin-top: 4px;
  }
  .card--front .wordmark {
    left: 0; right: 0; top: 110px;
    color: #ffffff;
  }
  .card--front .wordmark__square { background: #ffffff; }
  .card--back .wordmark {
    left: 90px; width: 260px; top: 120px;
    color: var(--brand-red);
  }
  .card--back .wordmark__square { background: var(--brand-red); width: 62px; height: 62px; }
  .card--back .wordmark__name { font-size: 56px; }
  .card--back .wordmark__sub { font-size: 21px; }

  .contact {
    position: absolute;
    left: 405px;
    top: 118px;
    font-family: "Saira Semi Condensed", sans-serif;
    color: var(--ink);
  }
  .contact__name {
    font-weight: 700;
    font-size: 36px;
    color: var(--brand-red);
    margin: 0;
    line-height: 1;
  }
  .contact__role {
    font-family: "Inter", sans-serif;
    font-size: 16px;
    color: var(--ink-soft);
    margin: 8px 0 22px 4px;
  }
  .contact__list {
    list-style: none;
    margin: 0;
    padding: 0;
  }
  .contact__item {
    display: flex;
    align-items: center;
    gap: 14px;
    font-size: 17px;
    font-weight: 500;
    height: 27px;
  }
  .contact__icon {
    width: 18px;
    height: 18px;
    fill: var(--brand-red);
    flex: none;
  }
</style>
</head>
<body>

<section class="card card--front">
  <div class="wordmark">
    <div class="wordmark__square"></div>
    <div class="wordmark__name">VARNO</div>
    <div class="wordmark__sub">Building Pty Ltd</div>
  </div>
</section>

<section class="card card--back">
  <div class="wordmark">
    <div class="wordmark__square"></div>
    <div class="wordmark__name">VARNO</div>
    <div class="wordmark__sub">Building Pty Ltd</div>
  </div>

  <div class="contact">
    <h1 class="contact__name">Liam Carter</h1>
    <p class="contact__role">Managing Director</p>
    <ul class="contact__list">
      <li class="contact__item">
        <svg class="contact__icon" viewBox="0 0 24 24"><path d="M3 9c0-3 4-5 9-5s9 2 9 5v2h-5V9H8v2H3z"/><rect x="5" y="12" width="14" height="8" rx="1"/></svg>
        1300 418 520
      </li>
      <li class="contact__item">
        <svg class="contact__icon" viewBox="0 0 24 24"><path d="M7 2h10a1 1 0 0 1 1 1v18a1 1 0 0 1-1 1H7a1 1 0 0 1-1-1V3a1 1 0 0 1 1-1zm1 3v13h8V5zm4 14.5a1 1 0 1 0 0 .01z"/></svg>
        0422 735 190
      </li>
      <li class="contact__item">
        <svg class="contact__icon" viewBox="0 0 24 24"><path d="M12 2a10 10 0 1 0 0 20 10 10 0 0 0 0-20zm-1 2.1V8H7.6A8 8 0 0 1 11 4.1zm2 0A8 8 0 0 1 16.4 8H13zM4.3 10H11v4H4.3a8 8 0 0 1 0-4zM13 10h6.7a8 8 0 0 1 0 4H13zM7.6 16H11v3.9A8 8 0 0 1 7.6 16zM13 16h3.4A8 8 0 0 1 13 19.9z"/></svg>
        www.varnobuilding.com.au
      </li>
      <li class="contact__item">
        <svg class="contact__icon" viewBox="0 0 24 24"><path d="M2 5h20v14H2zm2 2v.4l8 5.2 8-5.2V7zm0 2.8V17h16V9.8l-8 5.2z"/></svg>
        liam.carter@varnobuilding.com.au
      </li>
      <li class="contact__item">
        <svg class="contact__icon" viewBox="0 0 24 24"><path d="M12 2a7 7 0 0 0-7 7c0 5 7 13 7 13s7-8 7-13a7 7 0 0 0-7-7zm0 9.5A2.5 2.5 0 1 1 12 6.5a2.5 2.5 0 0 1 0 5z"/></svg>
        88 Harbour Lane, Sydney NSW 2000
      </li>
    </ul>
  </div>
</section>

</body>
</html>
```